Vexo Ledger Word Press Website Home Page, Form and Search Results Page

We are a website called "Vexo Ledger" (www.VexoLedger.com) that provides Audit Tests descriptions for Technology Auditors to use. The website is under construction, however I have a test website to give you a better idea: www.vexoledgerhub.org. I already have a logo and some icons that you'll be able to see at www.vexoledgerhub.org.

I'm looking for a WebPress design I can give to my web programmer to implement on HostPelican.

The central purpose of the website is to provide a place for auditors to find technology audit tests and for experienced auditors to add audit tests to the existing catalog of tests.

I'd like the website to be the gold standard in Technology Audit Tests so I will encourage auditors to edit the catalog of tests as well as submit new tests.

The Form to Add or Edit Audit Tests must include the following fields:
Field 1: Technology Type (i.e. Mainframe, Database, Network ...)
Field 2: Risk Description (i.e. Cyber Security Attack, Service Outage...)
Field 3: Control Description (i.e. Remove Leavers Access, Backup Data...)
Field 4: Audit Test (i.e. Check Leavers list with Access List, Check Backups can be Restored)
Field 5: Test Author Name (i.e. name of person that added the test)

Each audit test in the catalog will have information in the 5 fields above - this will give auditors what they need to know to perform an audit.Typically each audit test is displayed as a row in a table. For each technology type (i.e. Mainframe) there can be up to 30-40 tests. Together these tests form what's called an Audit Program (google will give you more info if you search for it).

I would like the Search results to also display the 5 fields above. For example if someone searches for "Backup" or "Mainframe" then the search result will show the 5 fields for each audit test relevant to "Backup" in a table format. I will limited the amount of text that can be added to each field so it can be displayed in a table on the web page.

The customer base is Technology Auditors and the website a place to them to find information about how to audit. Its important the website design looks modern, hi-tech and simple to use.

The visitors will come to the website typically audit cyber security, cloud computing, mainframes, payment systems etc hence it needs a high-tech feel.

As an example, a typically customer will be some that has been asked to audit a technology but has not done it before so they will come to the website to look for audit tests. The other type of customer will be someone that has just finished an audit and wants to share their tests that describes how they audited the technology.

It's important the website looks professional and gives a sense of trust as well as giving sense of high-tech, modern leading edge thinking.

In summary the website provides 4 things:
(1) An auditor can browse for audit tests by technology type (mainframe, database etc)
(2) Search for a test based on a criteria like "Cyber Security".
(3) Add/Submit an audit test or edit an existing test.
(4) Access other relevant auditor resources ( links and publications etc).

Target Market(s)

Professional Auditors that want to find information to help them in their day-to-day job.

Industry/Entity Type

Auditing

Logo Text

Vexo Ledger

Number of Pages Required

3 page

Font styles to use
Sans Serif

Requirements
Must have
• A Word Press Theme I can pass to my web programmer.
• I need 3 pages designed:
• (1) A Home Page
• (2) A Form to Submit Audit Tests (see 5 fields above in project description)
• (3) A Search Results Page that lists the results from Search (see 5 fields in project description)
• The Home should list a sample of the audit test in two ways:
• (1) include a league table on the home page with the top 10 most popular audit tests showing the author, test title, technology types, and risk title.
• (2) A selection of the icons in a square or regular pattern, similar to a list of products. These will essentially be feature audit tests. Once a visitor click the icon they will be taken through to a table that will list all the audit tests relevant to that feature technology category i.e. cyber, resilience, mainframe etc.
• The website must have a Modern, Hi-Tech Design that is simple to use.
• I like the modern colors in website slider image on www.vexoledgerhub.org
Nice to have
• Change color of icons (attached) to match the Logo and Slider image (both attached) as the orange and blue icons not match the logo.
Should not have
• The website will not have a Cart
• The website design must not be too busy or complicated.

```html
<!DOCTYPE html>
<html lang="en">
<head>
<meta charset="utf-8">
<title>Vexo Ledger — Home</title>
<link href="https://fonts.googleapis.com/css2?family=Barlow:wght@300;400;500;600;700&display=swap" rel="stylesheet">
<style>
:root{
  --teal:#0a9bb1;
  --teal-dark:#078396;
  --green:#4db66f;
  --blue:#2a8fd6;
  --orange:#ff9a0a;
  --red:#ff5a26;
  --ink:#3b4350;
  --muted:#8a919c;
  --line:#e3e7ed;
  --pale:#f4f7fb;
  --footer:#2b2e34;
  --white:#ffffff;
}
*{box-sizing:border-box;margin:0;padding:0}
html,body{width:1200px;height:2744px;overflow:hidden}
body{font-family:"Barlow",Arial,sans-serif;color:var(--ink);background:var(--white);position:relative}
.abs{position:absolute}
a{color:inherit;text-decoration:none}
h1,h2,h3{font-weight:400}

/* header */
.site-header{position:absolute;left:0;top:0;width:1200px;height:58px;background:var(--white)}
.brand{left:113px;top:13px;display:flex;align-items:center;gap:8px;font-size:27px;font-weight:500;color:var(--teal)}
.brand-dot{width:30px;height:30px;border-radius:50%;background:var(--teal)}
.main-nav{left:426px;top:20px;font-size:14px;letter-spacing:1.6px;font-weight:500;color:#4a525e}
.main-nav a{position:absolute;white-space:nowrap}
.search-icon{left:926px;top:18px}
.sign-in{left:978px;top:11px;width:109px;height:37px;background:var(--teal);color:#fff;font-size:13px;font-weight:600;letter-spacing:1.5px;display:flex;align-items:center;justify-content:center}

/* hero */
.hero{left:0;top:58px;width:1200px;height:553px;background:
 linear-gradient(90deg,#1a1f4a 0%,#3a2a6a 22%,#6a2a52 38%,#2b3d8e 52%,#1c2f78 68%,#0f2a8a 85%,#1337a8 100%)}
.hero-welcome{left:113px;top:186px;width:332px;height:32px;border-top:1px solid rgba(255,255,255,.8);border-bottom:1px solid rgba(255,255,255,.8);color:#fff;font-size:15px;letter-spacing:12px;text-align:center;line-height:30px;padding-left:12px}
.hero-title{left:113px;top:244px;color:#fff;font-size:42px;font-weight:300;letter-spacing:4px;line-height:51px}
.hero-title strong{font-weight:700}
.hero-btn{top:426px;height:40px;color:#fff;font-size:13px;letter-spacing:2px;display:flex;align-items:center;justify-content:center;border:2px solid #fff}
.hero-btn.outline{left:113px;width:220px}
.hero-btn.fill{left:351px;width:159px;background:var(--teal);border-color:#d8f4f8}

/* section titles */
.section-title{left:0;width:1200px;text-align:center;font-size:35px;font-weight:400;letter-spacing:3px;color:var(--teal)}

/* find program */
.find{left:0;top:611px;width:1200px;height:499px;background:var(--pale)}
.program-card{top:137px;width:218px;height:293px;background:#fff;border:1px solid var(--line)}
.program-head{height:84px;color:#fff;text-align:center;padding-top:19px}
.program-head .small{font-size:11px;letter-spacing:1.6px;display:inline-block;border-bottom:1px dashed rgba(255,255,255,.8);padding:0 4px 4px}
.program-head .big{font-size:15px;font-weight:600;letter-spacing:2px;margin-top:5px}
.program-list{list-style:none;margin:5px 0 0}
.program-list li{height:33px;line-height:33px;text-align:center;font-size:12px;letter-spacing:1.3px;color:var(--muted);border-bottom:1px solid #eef1f5;margin:0 4px}
.program-more{text-align:center;font-size:14px;letter-spacing:9px;color:var(--teal);margin-top:12px;padding-left:9px}
.program-btn{position:absolute;left:12px;right:12px;top:251px;height:33px;background:var(--teal);color:#fff;font-size:11px;letter-spacing:.6px;font-weight:500;display:flex;align-items:center;justify-content:center;border-radius:2px}
.tech .program-head{background:var(--green)}
.risk .program-head{background:var(--blue)}
.control .program-head{background:var(--orange)}
.audit .program-head{background:var(--red)}

/* features */
.feature-card{top:1233px;width:277px;height:245px;border:1px solid var(--line);background:#fff;text-align:center}
.feature-icon{position:absolute;left:86px;top:-51px;width:104px;height:104px;border-radius:8px}
.feature-title{position:absolute;left:0;right:0;top:80px;font-size:15px;letter-spacing:.6px;color:#4a525e}
.feature-text{position:absolute;left:30px;right:30px;top:112px;font-size:12.5px;line-height:20px;color:#a3a9b2}
.feature-btn{position:absolute;left:80px;top:175px;width:117px;height:37px;border:1.5px solid var(--teal);color:var(--teal);font-size:11px;letter-spacing:.6px;display:flex;align-items:center;justify-content:center}

/* publications */
.publications{left:0;top:1560px;width:1200px;height:512px;background:var(--teal)}
.publications .section-title{color:#fff}
.pub-image{top:137px;width:306px;height:169px;border:2px solid #fff}
.pub-card{top:267px;width:280px;height:176px;background:#fff;border-radius:6px 6px 0 0;padding:20px 22px}
.pub-meta{display:flex;justify-content:space-between;font-size:11px;color:var(--muted)}
.pub-meta .date{color:var(--teal)}
.pub-title{font-size:16px;line-height:19px;font-weight:400;color:#3b4350;margin-top:14px}
.pub-text{font-size:12.5px;line-height:15px;color:var(--muted);margin-top:8px}
.pub-link{display:inline-block;font-size:11px;color:var(--teal);border-bottom:1px solid var(--teal);padding-bottom:3px;margin-top:9px;letter-spacing:.4px}

/* popular docs */
.slider-arrow{top:2261px;width:38px;height:37px;background:#7fc7d9;display:flex;align-items:center;justify-content:center}
.doc-card{top:2202px;width:391px;height:154px;background:var(--pale);padding:23px 0 0 84px}
.doc-thumb{top:2228px;width:104px;height:102px;border-radius:8px}
.doc-time{font-size:11px;color:var(--teal);display:flex;align-items:center;gap:8px}
.doc-title{font-size:17px;font-weight:400;color:#3b4350;margin-top:10px}
.doc-text{font-size:12.5px;line-height:19px;color:var(--muted);margin-top:6px;width:290px}

/* about */
.about{left:0;top:2433px;width:1200px;height:250px;background:var(--pale)}
.about-text{left:256px;top:2563px;width:688px;text-align:center;font-size:13.5px;line-height:23px;color:var(--muted)}

/* footer */
.site-footer{left:0;top:2683px;width:1200px;height:61px;background:var(--footer);color:#fff;font-size:11.5px}
.footer-links a{position:absolute;top:26px;white-space:nowrap}
.copyright{left:646px;top:26px}
.follow{left:856px;top:24px;font-size:13px}
.social{top:2700px;width:28px;height:28px}
</style>
</head>
<body>

<header class="site-header">
  <a class="brand abs" href="#"><span class="brand-dot"></span>Vexo Ledger</a>
  <nav class="main-nav abs">
    <a href="#" style="left:0">BROWSE</a>
    <a href="#" style="left:95px">SEARCH</a>
    <a href="#" style="left:189px">ADD</a>
    <a href="#" style="left:254px">CONTACT US</a>
  </nav>
  <svg class="search-icon abs" width="22" height="22" viewBox="0 0 22 22" aria-label="Search"><circle cx="9" cy="9" r="6.5" fill="none" stroke="#0a9bb1" stroke-width="2"/><line x1="14" y1="14" x2="20" y2="20" stroke="#0a9bb1" stroke-width="2.4" stroke-linecap="round"/></svg>
  <a class="sign-in abs" href="#">SIGN IN</a>
</header>

<section class="hero abs" role="img" aria-label="Engineer working at a lit server rack in a data centre"></section>
<div class="hero-welcome abs">WELCOME</div>
<h1 class="hero-title abs">YOUR DEFINITIVE<br>GUIDE TO<br><strong>TECHNOLOGY AUDIT</strong></h1>
<a class="hero-btn outline abs" href="#">AUDITS PROGRAMS</a>
<a class="hero-btn fill abs" href="#">RESOURCES</a>

<section class="find abs">
  <h2 class="section-title abs" style="top:58px">FIND AN AUDIT PROGRAM</h2>

  <div class="program-card tech abs" style="left:113px">
    <div class="program-head"><span class="small">VIEW BY</span><div class="big">TECHNOLOGY</div></div>
    <ul class="program-list"><li>OPERATING SYSTEM</li><li>DATABASE</li><li>NETWORK</li></ul>
    <div class="program-more">MORE</div>
    <a class="program-btn" href="#">GET STARTED</a>
  </div>
  <div class="program-card risk abs" style="left:365px">
    <div class="program-head"><span class="small">VIEW BY</span><div class="big">RISK</div></div>
    <ul class="program-list"><li>CYBER</li><li>DATA LOSS</li><li>SERVICE OUTAGE</li></ul>
    <div class="program-more">MORE</div>
    <a class="program-btn" href="#">GET STARTED</a>
  </div>
  <div class="program-card control abs" style="left:617px">
    <div class="program-head"><span class="small">VIEW BY</span><div class="big">CONTROL</div></div>
    <ul class="program-list"><li>PENETRATION TEST</li><li>RESILVENCE</li><li>AUTHENTICATION</li></ul>
    <div class="program-more">MORE</div>
    <a class="program-btn" href="#">GET STARTED</a>
  </div>
  <div class="program-card audit abs" style="left:869px">
    <div class="program-head"><span class="small">VIEW BY</span><div class="big">AUDIT</div></div>
    <ul class="program-list"><li>GENERAL AUDIT</li><li>INFRUSTRUCTURE AUDIT</li><li>APPLICATION AUDIT</li></ul>
    <div class="program-more">MORE</div>
    <a class="program-btn" href="#">GET STARTED</a>
  </div>
</section>

<div class="feature-card abs" style="left:113px">
  <div class="feature-icon" role="img" aria-label="Magnifying glass icon" style="background:linear-gradient(135deg,#f06a5a,#d9473a)"></div>
  <div class="feature-title">SEARCH FOR AUDIT TESTS</div>
  <p class="feature-text">Search the full range of Technology audit tests in the Catalog.</p>
  <a class="feature-btn" href="#">VIEW MORE</a>
</div>
<div class="feature-card abs" style="left:461px">
  <div class="feature-icon" role="img" aria-label="Microchip icon" style="background:linear-gradient(135deg,#ffc23a,#f08a10)"></div>
  <div class="feature-title">BROWSE CALOG AUDIT TESTS</div>
  <p class="feature-text">A range of popular Technology Audit Tests for use in auditing various technologies</p>
  <a class="feature-btn" href="#">VIEW MORE</a>
</div>
<div class="feature-card abs" style="left:809px">
  <div class="feature-icon" role="img" aria-label="Tools and server icon" style="background:linear-gradient(135deg,#2a8fe0,#1560b0)"></div>
  <div class="feature-title">ADDITIONAL AUDITOR RESOURCES</div>
  <p class="feature-text">Audit Templates, Frameworks and Links to other useful sites.</p>
  <a class="feature-btn" href="#">VIEW MORE</a>
</div>

<section class="publications abs">
  <h2 class="section-title abs" style="top:58px">LATEST PUBLICATION</h2>

  <div class="pub-image abs" style="left:113px;background:linear-gradient(135deg,#0b5a6a,#2bb6c8 55%,#0a3f55)" role="img" aria-label="Digital head over circuit board"></div>
  <div class="pub-image abs" style="left:447px;background:radial-gradient(ellipse at 50% 90%,#dff4ff,#4aa8f0 30%,#0b2a6a 70%,#05163a)" role="img" aria-label="Burst of light in digital data stream"></div>
  <div class="pub-image abs" style="left:781px;background:radial-gradient(ellipse at 50% 50%,#0a1a5a,#1f4fd8 50%,#7fb0ff 80%,#1c3aa8)" role="img" aria-label="Binary code tunnel"></div>

  <article class="pub-card abs" style="left:126px">
    <div class="pub-meta"><span>BY ADMIN</span><span class="date">17 JULY 2015</span></div>
    <h3 class="pub-title">4 Springtime Color Schemes to Try at Home</h3>
    <p class="pub-text">Brightmoor Construction LTD is a London based developer and contractor...</p>
    <a class="pub-link" href="#">READ MORE</a>
  </article>
  <article class="pub-card abs" style="left:460px">
    <div class="pub-meta"><span>BY ADMIN</span><span class="date">17 JULY 2015</span></div>
    <h3 class="pub-title">4 Springtime Color Schemes to Try at Home</h3>
    <p class="pub-text">Brightmoor Construction LTD is a London based developer and contractor...</p>
    <a class="pub-link" href="#">READ MORE</a>
  </article>
  <article class="pub-card abs" style="left:794px">
    <div class="pub-meta"><span>BY ADMIN</span><span class="date">17 JULY 2015</span></div>
    <h3 class="pub-title">4 Springtime Color Schemes to Try at Home</h3>
    <p class="pub-text">Brightmoor Construction LTD is a London based developer and contractor...</p>
    <a class="pub-link" href="#">READ MORE</a>
  </article>
</section>

<h2 class="section-title abs" style="top:2130px">POPULAR DOCUMENTS</h2>
<a class="slider-arrow abs" style="left:49px" href="#" aria-label="Previous"><svg width="16" height="16" viewBox="0 0 16 16"><path d="M14 8H3M8 3L3 8l5 5" fill="none" stroke="#fff" stroke-width="2.4"/></svg></a>
<a class="slider-arrow abs" style="left:1112px" href="#" aria-label="Next"><svg width="16" height="16" viewBox="0 0 16 16"><path d="M2 8h11M8 3l5 5-5 5" fill="none" stroke="#fff" stroke-width="2.4"/></svg></a>

<article class="doc-card abs" style="left:166px">
  <div class="doc-time"><svg width="12" height="12" viewBox="0 0 12 12"><circle cx="6" cy="6" r="5" fill="none" stroke="#8a919c"/><path d="M6 3v3l2 1" fill="none" stroke="#8a919c"/></svg>12 hours ago</div>
  <h3 class="doc-title">Software Developer/Analyst</h3>
  <p class="doc-text">Brightmoor Construction LTD is a London based developer and contractor Brightmoor Construction LTD is a London based developer....</p>
</article>
<div class="doc-thumb abs" style="left:112px;background:linear-gradient(135deg,#9fd0ff,#2f6fd8 55%,#1a3a9a)" role="img" aria-label="Glowing processor chip"></div>

<article class="doc-card abs" style="left:696px">
  <div class="doc-time"><svg width="12" height="12" viewBox="0 0 12 12"><circle cx="6" cy="6" r="5" fill="none" stroke="#8a919c"/><path d="M6 3v3l2 1" fill="none" stroke="#8a919c"/></svg>12 hours ago</div>
  <h3 class="doc-title">Software Developer/Analyst</h3>
  <p class="doc-text">Brightmoor Construction LTD is a London based developer and contractor Brightmoor Construction LTD is a London based developer....</p>
</article>
<div class="doc-thumb abs" style="left:641px;background:linear-gradient(135deg,#1e4fc8,#0a2a8a 50%,#3b7ae0)" role="img" aria-label="Blue circuit board"></div>

<section class="about abs">
  <h2 class="section-title abs" style="top:70px">ABOUT US</h2>
</section>
<p class="about-text abs">Vexo Ledger is the premium source of Technology Audit knowledge, tools and templates for use by Audit Professionals. We are a Global group of experienced Auditors professionals that have come together to promote leading edge best practice.</p>

<footer class="site-footer abs">
  <nav class="footer-links">
    <a href="#" style="left:112px">Terms of Use</a>
    <a href="#" style="left:204px">Disclaimer</a>
    <a href="#" style="left:284px">Privacy Policy</a>
    <a href="#" style="left:376px">Contact Us</a>
    <a href="#" style="left:457px">About Us</a>
    <a href="#" style="left:528px">Site Map</a>
  </nav>
  <div class="copyright abs">Copyright © 2015 Vexo Ledger.</div>
  <div class="follow abs">Follow us on</div>
</footer>
<span class="social abs" style="left:950px;background:#2e9fdc"></span>
<span class="social abs" style="left:987px;background:#f07a22"></span>
<span class="social abs" style="left:1024px;background:#e0463a"></span>
<span class="social abs" style="left:1061px;background:#1f7ab8"></span>

</body>
</html>
```